Holiday Rental Company Flyer Design (DL not A5)

Note from PixelFolk Administration: The category sizing selected is A5, however the project requires DL sized artwork. Please refer to the DL template link below while the 'Special Requirements' are updated accordingly.

Project Brief:
We need a double sided DL flyer designed for an up market Holiday Rental Company that portrays a personalised approach to property management. These are to be used for letter box drops to homes we're specifically targeting so the design should be modern, complimentary colour palette, uncluttered & visually appealing.

Please Download the DL Template from Quillmark here: http://www.quillmark.com.au/qm/ns/propath/UploadResources.aspx?selectedTab=0?pfid=BFB&pf_id=BFB&xnav=easypath-upload-image#Templates

Target Market(s)

Wealthy Home Owners

Industry/Entity Type

It Company

Font styles to use
Other font styles liked:
• Avant Garde Extra Light & Demi

Colors
33b8a4

Requirements
Must have
• DL Flyer sizes (210mm width x 99mm width, plus 3mm bleed)
• Front: Logo, Main Image & Grab
• Back: Contact Details & Brief Description of our business
• Images: Ideally the main image should be the house with the pool but alternatively a lifestyle images could also be used.
Nice to have
• A creative designer!
Should not have
• Clutter & busy designs

```html
<!DOCTYPE html>
<html lang="en">
<head>
<meta charset="utf-8">
<title>Headland Retreats – DL Flyer</title>
<link rel="stylesheet" href="https://fonts.googleapis.com/css2?family=Poppins:ital,wght@0,200;0,300;1,200;1,300;1,600&display=swap">
<style>
  :root {
    --teal: #27b5a3;
    --teal-deep: #1f9e8d;
    --teal-band: #2aa38f;
    --white: #ffffff;
    --ink: #3a3a3a;
    --stage: #2a2a2a;
    --rule-grey: #c9cccc;
  }
  * { margin: 0; padding: 0; box-sizing: border-box; }
  html, body {
    width: 1074px; height: 1200px; overflow: hidden;
    background: var(--stage);
    font-family: "Poppins", sans-serif;
  }
  .sheet { position: relative; width: 1074px; height: 1200px; }
  .flyer {
    position: absolute; top: 111px; width: 461px; height: 980px;
    background: var(--teal); overflow: hidden; color: var(--white);
  }
  .flyer--front { left: 39px; }
  .flyer--back { left: 531px; }

  /* Front */
  .front-name {
    position: absolute; top: 52px; left: 0; width: 100%;
    text-align: center; font-weight: 200; font-size: 58px;
    line-height: 66px; letter-spacing: 5px; text-transform: uppercase;
  }
  .front-mark {
    position: absolute; top: 218px; left: 50%; width: 110px; height: 110px;
    margin-left: -55px; border: 2px solid var(--white); border-radius: 50%;
  }
  .front-shapes { position: absolute; top: 0; left: 0; }
  .front-tagline {
    position: absolute; top: 860px; left: 0; width: 100%;
    text-align: center; font-style: italic; font-weight: 300;
    font-size: 25px; line-height: 37px;
  }
  .front-url {
    position: absolute; bottom: 0; left: 0; width: 100%; height: 36px;
    background: var(--teal-deep); text-align: center;
    font-weight: 300; font-size: 15px; line-height: 36px; letter-spacing: 2.5px;
  }

  /* Back */
  .back-header { position: absolute; top: 0; left: 0; width: 100%; height: 120px;
    display: flex; align-items: center; justify-content: center; gap: 16px; }
  .back-header__dot { width: 54px; height: 54px; border: 2px solid var(--white); border-radius: 50%; }
  .back-header__name { font-weight: 200; font-size: 34px; line-height: 38px;
    letter-spacing: 3px; text-transform: uppercase; }
  .back-heading { position: absolute; top: 120px; left: 0; width: 100%; height: 67px;
    background: var(--teal-band); text-align: center; font-style: italic;
    font-weight: 300; font-size: 28px; line-height: 67px; }
  .back-body { position: absolute; top: 187px; left: 0; width: 100%; height: 418px;
    background: var(--white); color: var(--ink); padding: 16px 32px 0;
    font-style: italic; font-weight: 300; font-size: 19px; line-height: 28px; text-align: justify; }
  .back-body p { margin-bottom: 12px; }
  .back-body .highlight { color: var(--teal); font-weight: 600; }
  .back-body ul { list-style: none; margin-top: 18px; }
  .gallery { position: absolute; top: 605px; left: 0; width: 100%; height: 130px;
    border-top: 12px solid var(--teal); border-bottom: 12px solid var(--teal);
    display: flex; }
  .gallery__photo { flex: 1; height: 100%; }
  .gallery__photo--bedroom { background: linear-gradient(135deg, #e6d6b8, #c9b98a 50%, #d45a4a); }
  .gallery__photo--bay { background: linear-gradient(180deg, #b9d3dc, #7fb4c6 55%, #5aa2b8); }
  .gallery__photo--interior { background: linear-gradient(90deg, #c8602f, #8a8f86 50%, #d8d2c4); }
  .back-prompt { position: absolute; top: 735px; left: 0; width: 100%; height: 120px;
    background: var(--white); color: var(--ink); text-align: center;
    font-style: italic; font-weight: 300; font-size: 19px; line-height: 28px; padding-top: 24px; }
  .back-contact { position: absolute; top: 855px; left: 0; width: 100%; height: 125px;
    background: var(--teal-deep); text-align: center; font-weight: 300;
    font-size: 16px; line-height: 25px; letter-spacing: 2.2px; padding-top: 9px; }
</style>
</head>
<body>
<main class="sheet">
  <section class="flyer flyer--front">
    <svg class="front-shapes" width="461" height="980" viewBox="0 0 461 980">
      <defs>
        <linearGradient id="poolHouse" x1="0" y1="0" x2="0.6" y2="1">
          <stop offset="0" stop-color="#c9a56a"/>
          <stop offset="0.45" stop-color="#3a3452"/>
          <stop offset="0.8" stop-color="#2b3f8a"/>
          <stop offset="1" stop-color="#3fb4e8"/>
        </linearGradient>
      </defs>
      <polygon points="160,395 461,362 461,368 175,398" fill="var(--rule-grey)"/>
      <polygon points="210,405 461,372 461,440" fill="var(--white)"/>
      <polygon points="0,428 461,395 461,785 0,830" fill="url(#poolHouse)" role="img" aria-label="Photograph of a modern house with lit pool at dusk"/>
    </svg>
    <h1 class="front-name">Headland<br>Retreats</h1>
    <div class="front-mark"></div>
    <p class="front-tagline">Holiday Rental Management<br>with a difference</p>
    <p class="front-url">www.headlandretreats.com.au</p>
  </section>

  <section class="flyer flyer--back">
    <header class="back-header">
      <span class="back-header__dot"></span>
      <span class="back-header__name">Headland<br>Retreats</span>
    </header>
    <h2 class="back-heading">What we do differently!</h2>
    <div class="back-body">
      <p>Rather than relying upon a key safe or a central pick-up destination, a ‘Headland Retreats’ staff member will greet guests upon arrival.</p>
      <p>Our <span class="highlight">‘Meet &amp; Greet’</span> service provides home owners with an increased level of Security and also allows us to:</p>
      <ul>
        <li>Prepare the home for their arrival (lights, heaters, music etc.)</li>
        <li>Establish a rapport &amp; help facilitate future bookings.</li>
        <li>Reiterate their responsibilities to ensure the return of their bond</li>
      </ul>
    </div>
    <div class="gallery">
      <div class="gallery__photo gallery__photo--bedroom" role="img" aria-label="Bedroom with bright cushions"></div>
      <div class="gallery__photo gallery__photo--bay" role="img" aria-label="Calm bay with a moored sailing boat"></div>
      <div class="gallery__photo gallery__photo--interior" role="img" aria-label="Interior with flowers in a vase"></div>
    </div>
    <p class="back-prompt">If you’d like to know what your property<br>could achieve or require additional<br>information, please contact us on:</p>
    <address class="back-contact" style="font-style:normal">
      PO Box 12, Shoreview Victoria 3900<br>
      (03)5550 0142<br>
      stay@headlandretreats.com.au<br>
      www.headlandretreats.com.au
    </address>
  </section>
</main>
</body>
</html>
```